Event Manager Business Card Design

I am a freelance event manager and work on high end events such as film premieres, product launches and black tie charity dinners. I would like the design to reflect efficiency, reliability, creativity and passion. I am a French Canadian who is now living and working in Sydney, Australia and although I will not be doing any business in Canada, perhaps a Canadian element can be incorporated in the business card to make my card stand out? I would like there to be some white space on the card to allow people to write on it, but not too much. I also want both sides of the card to be used. As a freelancer, I will be handing out my card to anyone with an outstretched hand. It's safe to assume that anyone who gets my card will be receiving hundreds of business cards at a time, so I really need mine to stand out. Please be original! I kind of want people reaction when they receive my card to be "wow, this guy means business, cool card".

Industry/Entity Type

Charity

Contact Information for Business Card

Marc Velline
Event Manager
+61 437 602 915
mvelline4@quorvix.com
brentlo.com/in/marcvelline

Requirements
Should not have
• Cliché event management elements (no film reels, no top hats, etc.)

```html
<!DOCTYPE html>
<html lang="en">
<head>
<meta charset="utf-8">
<title>Marc Velline — Event Manager Business Card</title>
<link href="https://fonts.googleapis.com/css2?family=Orbitron:wght@500;700&family=Montserrat:wght@400;500&display=swap" rel="stylesheet">
<style>
  :root {
    --backdrop: #e4e4e6;
    --card: #ffffff;
    --ink: #111111;
    --muted: #666666;
    --navy: #3b3c6e;
    --silver: #b9b8bc;
    --rule: #4a4b70;
    --pattern-light: #dcdce8;
  }
  html, body {
    margin: 0;
    padding: 0;
    width: 1200px;
    height: 900px;
    overflow: hidden;
    background: var(--backdrop);
  }
  .stage {
    position: relative;
    width: 1200px;
    height: 900px;
  }
  .card {
    position: absolute;
    width: 617px;
    height: 338px;
    background: var(--card);
    border-radius: 14px;
    overflow: hidden;
    box-shadow: 0 3px 10px rgba(0,0,0,0.18);
  }
  .card--front { left: 103px; top: 72px; }
  .card--back  { left: 484px; top: 482px; }
  .card-art {
    position: absolute;
    inset: 0;
    width: 100%;
    height: 100%;
  }
  .identity {
    position: absolute;
    left: 318px;
    top: 78px;
  }
  .identity__name {
    margin: 0;
    font-family: "Orbitron", sans-serif;
    font-weight: 700;
    font-size: 34px;
    line-height: 1;
    color: var(--ink);
    letter-spacing: 0.5px;
  }
  .identity__role {
    margin: 4px 0 0 2px;
    font-family: "Orbitron", sans-serif;
    font-weight: 500;
    font-size: 15px;
    color: var(--muted);
    letter-spacing: 0.5px;
  }
  .contact-list {
    position: absolute;
    right: 18px;
    top: 162px;
    margin: 0;
    padding: 0;
    list-style: none;
    font-family: "Montserrat", sans-serif;
    font-size: 12.5px;
    color: #333;
    letter-spacing: 1px;
    text-align: right;
  }
  .contact-list li {
    display: flex;
    justify-content: flex-end;
    align-items: center;
    gap: 6px;
    height: 16.5px;
  }
  .contact-icon {
    width: 10px;
    height: 10px;
    flex: none;
  }
  .notes {
    position: absolute;
    left: 28px;
    top: 53px;
    width: 312px;
  }
  .notes__line {
    height: 1px;
    background: var(--rule);
    margin-bottom: 40px;
  }
  .notes__line:nth-child(4) { margin-top: 4px; }
  .back-email {
    position: absolute;
    left: 28px;
    width: 312px;
    top: 203px;
    text-align: center;
    font-family: "Montserrat", sans-serif;
    font-size: 12.5px;
    letter-spacing: 1.6px;
    color: #444;
  }
</style>
</head>
<body>
<main class="stage">

  <section class="card card--front" aria-label="Business card front">
    <svg class="card-art" viewBox="0 0 617 338" aria-hidden="true">
      <defs>
        <linearGradient id="frontPatternTone" x1="0" y1="0" x2="0" y2="1">
          <stop offset="0" stop-color="var(--pattern-light)"/>
          <stop offset="0.6" stop-color="#8e8fb2"/>
          <stop offset="1" stop-color="var(--navy)"/>
        </linearGradient>
      </defs>
      <path d="M0,103 C200,140 400,300 617,270 L617,338 L0,338 Z" fill="var(--silver)"/>
      <path d="M0,119 C200,158 400,308 617,277 L617,338 L0,338 Z" fill="var(--card)"/>
      <path d="M0,129 C200,170 400,316 617,281 L617,338 L0,338 Z" fill="var(--navy)"/>
      <path d="M0,142 C200,186 400,326 617,289 L617,338 L0,338 Z" fill="var(--card)"/>
    </svg>
    <svg class="card-art" viewBox="0 0 617 338" role="img" aria-label="Halftone dot wave pattern in navy">
      <path d="M0,160 C200,208 400,334 617,296 L617,338 L0,338 Z" fill="url(#frontPatternTone)"/>
    </svg>

    <div class="identity">
      <h1 class="identity__name">Marc Velline</h1>
      <p class="identity__role">Event Manager</p>
    </div>

    <ul class="contact-list">
      <li>+61 437 602 915
        <svg class="contact-icon" viewBox="0 0 10 10" aria-hidden="true"><path d="M2.2,0.6 L3.8,2.6 L2.9,3.7 C3.5,5 4.8,6.4 6.2,7.1 L7.3,6.2 L9.4,7.7 L8.4,9.4 C4.6,9.2 0.7,5.3 0.6,1.6 Z" fill="var(--ink)"/></svg>
      </li>
      <li>mvelline4@quorvix.com
        <svg class="contact-icon" viewBox="0 0 10 10" aria-hidden="true"><rect x="0.5" y="2" width="9" height="6.4" fill="var(--ink)"/><path d="M0.8,2.4 L5,5.6 L9.2,2.4" stroke="#fff" stroke-width="0.9" fill="none"/></svg>
      </li>
      <li>brentlo.com/in/marcvelline
        <svg class="contact-icon" viewBox="0 0 10 10" aria-hidden="true"><rect x="0.5" y="0.5" width="9" height="9" fill="var(--ink)"/></svg>
      </li>
    </ul>
  </section>

  <section class="card card--back" aria-label="Business card back">
    <svg class="card-art" viewBox="0 0 617 338" aria-hidden="true">
      <defs>
        <linearGradient id="backPatternTone" x1="0" y1="0" x2="0" y2="1">
          <stop offset="0" stop-color="var(--pattern-light)"/>
          <stop offset="0.5" stop-color="#8e8fb2"/>
          <stop offset="1" stop-color="var(--navy)"/>
        </linearGradient>
      </defs>
      <path d="M0,282 C230,280 430,190 617,104 L617,338 L0,338 Z" fill="var(--silver)"/>
      <path d="M0,294 C230,292 430,206 617,124 L617,338 L0,338 Z" fill="var(--card)"/>
      <path d="M0,302 C230,300 430,214 617,132 L617,338 L0,338 Z" fill="var(--navy)"/>
      <path d="M0,312 C230,312 430,226 617,146 L617,338 L0,338 Z" fill="var(--card)"/>
    </svg>
    <svg class="card-art" viewBox="0 0 617 338" role="img" aria-label="Halftone dot wave pattern in navy">
      <path d="M0,322 C230,322 430,238 617,160 L617,338 L0,338 Z" fill="url(#backPatternTone)"/>
    </svg>

    <div class="notes" aria-label="Space for notes">
      <div class="notes__line"></div>
      <div class="notes__line"></div>
      <div class="notes__line"></div>
      <div class="notes__line"></div>
    </div>
    <p class="back-email">mvelline4@quorvix.com</p>
  </section>

</main>
</body>
</html>
```